Small, static, 2 page website that promotes 3-6 workshops

This is a microsite for my company that promotes 3 (and later 6) security workshops for developers. The address is going to be vakwerk-leerlijnen.nl so it is very important that the title reads 'Vakwerk Leerlijnen' and the subtitle reads 'voor ontwikkelaars' (means for developers in dutch).

On the frontpage, there will be a small introduction text (about 50 words) about the workshops in general and there should be 3 workshops listed on the frontpage with also a small introduction text. All the workshops are cyber security/hacking related so maybe a small graphic for every workshop would lighten things up.

Then when a visitor clicks a 'more info' button a detail page about that specific workshop with a longer description, a date/location, a 'book now' button and a price should be show.

I have include a quick drawing of what I have in mind for the frontpage, this is not set in stone so you could come up with something else.

I also included my company logo, it should be clear on the site that these workshops are 'Brightmoor Labs' workshops.

Target Market(s)

Development companies looking for security workshops, the responsible people for those type of workshops are usually security officers, lead developers/managers or developers themselves.

Industry/Entity Type

It Company

Number of Pages Required

2 page

Font styles to use
Sans Serif
Other font styles liked:
• Please choose a font you

Requirements
Must have
• 3 highlighted trainings on the frontpage and a detail page and the title and subtitle as headings on the page.
Nice to have
• I'd really like to have the 3 boxes on the frontpage to have icons or some sort of images. The first 3 workshops that are going to be on the page are:
• - Security awareness for developers
• - Web application security from a hackers perspective
• - Penetrationtesting for developers

```html
<!DOCTYPE html>
<html lang="nl">
<head>
<meta charset="utf-8">
<title>Vakwerk Leerlijnen – Security awareness for developers</title>
<link href="https://fonts.googleapis.com/css2?family=Roboto+Condensed:wght@300;400;700&display=swap" rel="stylesheet">
<style>
  :root {
    --navy: #1b3f6e;
    --navy-deep: #17375f;
    --text: #5a5a5a;
    --panel: #f6f5f5;
    --panel-line: #dcdcdc;
    --white: #ffffff;
    --logo-bg: #e6e9ed;
  }
  * { margin: 0; padding: 0; box-sizing: border-box; }
  html, body { width: 1200px; height: 978px; overflow: hidden; background: var(--white); }
  body { position: relative; font-family: "Roboto Condensed", Arial, sans-serif; color: var(--text); }

  .hero {
    position: absolute; left: 0; top: 0; width: 1200px; height: 236px;
    background:
      radial-gradient(ellipse 420px 200px at 560px 190px, rgba(205,215,228,0.9), rgba(205,215,228,0) 70%),
      linear-gradient(90deg, #8a9bb4 0%, #9fb0c6 30%, #8597b1 65%, #3d5578 100%);
  }
  .brand {
    position: absolute; left: 461px; top: 0; width: 279px; height: 91px;
    background: var(--logo-bg); border-radius: 0 0 4px 4px;
    display: flex; align-items: center; justify-content: center; gap: 10px;
  }
  .brand-dot { width: 26px; height: 26px; border-radius: 50%; background: var(--navy); }
  .brand-name { font-size: 26px; font-weight: 700; color: var(--navy); letter-spacing: 0.5px; text-transform: uppercase; }
  .hero-title {
    position: absolute; left: 0; width: 1200px; top: 146px; text-align: center;
    font-size: 31px; font-weight: 700; color: var(--white); text-transform: uppercase;
    text-shadow: 0 1px 3px rgba(0,0,0,0.35);
  }
  .hero-subtitle {
    position: absolute; left: 0; width: 1196px; top: 183px; text-align: center;
    font-size: 14.5px; font-weight: 400; color: var(--white); text-transform: uppercase;
    text-shadow: 0 1px 2px rgba(0,0,0,0.3);
  }

  .page-bar { position: absolute; left: 0; top: 236px; width: 1200px; height: 75px; background: var(--navy); }
  .page-bar .shield { position: absolute; left: 161px; top: 21px; }
  .page-title { position: absolute; left: 207px; top: 28px; font-size: 17px; font-weight: 300; color: var(--white); text-transform: uppercase; }
  .home-link { position: absolute; left: 994px; top: 32px; font-size: 11px; color: var(--white); text-transform: uppercase; display: flex; align-items: center; gap: 5px; }

  .workshop-media { position: absolute; left: 161px; top: 349px; width: 274px; height: 188px; border: 1px solid var(--navy); }
  .workshop-media .photo {
    position: absolute; left: 12px; top: 9px; width: 248px; height: 168px;
    background: radial-gradient(ellipse at 50% 35%, #5d6c73, #2a3338 75%);
  }

  .workshop-heading { position: absolute; left: 460px; top: 345px; font-size: 19.5px; font-weight: 300; color: var(--navy); }
  .workshop-heading::after { content: ""; position: absolute; left: 0; top: 28px; width: 44px; height: 1px; background: var(--navy); }

  .workshop-facts {
    position: absolute; left: 461px; top: 389px; width: 578px; height: 49px;
    background: var(--panel); border: 1px solid var(--panel-line);
  }
  .fact { position: absolute; top: 8px; display: flex; align-items: center; gap: 9px; font-size: 12.5px; color: var(--text); }
  .fact .icon { width: 32px; height: 32px; border-radius: 50%; background: var(--navy); display: flex; align-items: center; justify-content: center; }
  .fact-date { left: 10px; }
  .fact-place { left: 230px; }
  .fact-price { left: 440px; }

  .book-button {
    position: absolute; left: 894px; top: 458px; width: 145px; height: 35px;
    background: var(--navy-deep); color: var(--white); border-radius: 2px;
    font-size: 12.5px; font-weight: 700; text-transform: uppercase;
    display: flex; align-items: center; justify-content: center;
  }

  .workshop-body { position: absolute; left: 461px; top: 513px; width: 578px; }
  .workshop-body p { font-size: 12.5px; line-height: 15.8px; text-align: justify; margin-bottom: 15.8px; hyphens: auto; }

  .site-footer {
    position: absolute; left: 0; top: 925px; width: 1200px; height: 53px;
    background: var(--navy); color: var(--white); font-size: 11.5px;
    display: flex; align-items: center; justify-content: center;
  }
</style>
</head>
<body>
  <header class="hero" role="img" aria-label="Header photo: hand pointing at glowing security code digits on a blue-grey background">
    <div class="brand">
      <span class="brand-dot"></span>
      <span class="brand-name">Brightmoor Labs</span>
    </div>
    <h1 class="hero-title">Vakwerk Leerlijnen</h1>
    <p class="hero-subtitle">voor ontwikkelaars</p>
  </header>

  <nav class="page-bar">
    <svg class="shield" width="34" height="40" viewBox="0 0 34 40">
      <path d="M17 2 L31 8 V20 C31 29 24 35 17 38 C10 35 3 29 3 20 V8 Z" fill="none" stroke="#fff" stroke-width="2.4"/>
      <path d="M12 15 L8 20 L12 25 M22 15 L26 20 L22 25 M19 14 L15 26" fill="none" stroke="#fff" stroke-width="1.8" stroke-linecap="round"/>
    </svg>
    <h2 class="page-title">Security awareness for developers</h2>
    <span class="home-link">
      <svg width="11" height="9" viewBox="0 0 11 9"><path d="M5.5 0 L11 4.5 H9.5 V9 H6.5 V6 H4.5 V9 H1.5 V4.5 H0 Z" fill="#fff"/></svg>
      Home
    </span>
  </nav>

  <main>
    <figure class="workshop-media">
      <div class="photo" role="img" aria-label="Photo of a developer at a keyboard with hand-drawn device and platform sketches"></div>
    </figure>

    <h3 class="workshop-heading">Lorem Ipsum is simply dummy text</h3>

    <div class="workshop-facts">
      <div class="fact fact-date">
        <span class="icon"><svg width="14" height="14" viewBox="0 0 14 14"><rect x="1" y="2.5" width="12" height="10.5" fill="none" stroke="#fff" stroke-width="1.4"/><rect x="1" y="2.5" width="12" height="2.5" fill="#fff"/><path d="M4 1v3M10 1v3M1 8h12M1 10.5h12M5 5v8M9 5v8" stroke="#fff" stroke-width="1"/></svg></span>
        16/12/2016
      </div>
      <div class="fact fact-place">
        <span class="icon"><svg width="12" height="16" viewBox="0 0 12 16"><path d="M6 0 C9.3 0 12 2.6 12 5.8 C12 10 6 16 6 16 C6 16 0 10 0 5.8 C0 2.6 2.7 0 6 0 Z" fill="#fff"/><circle cx="6" cy="5.8" r="2.2" fill="#1b3f6e"/></svg></span>
        INDIA
      </div>
      <div class="fact fact-price">
        <span class="icon" style="color:#fff;font-weight:700;font-size:17px;">$</span>
        2000.00
      </div>
    </div>

    <a class="book-button">Book now</a>

    <section class="workshop-body">
      <p>Lorem ipsum dolor sit amet, consectetur adipiscing elit. Cras metus mi, interdum sit amet fermentum non, elementum at nibh. Nulla facilisi. Morbi mollis quis nisi non sagittis. Nullam pellentesque dui tortor, eu cursus libero maximus sed. Vestibulum rhoncus elementum ipsum ac bibendum. Mauris massa justo, ultrices eget quam eget, tincidunt pharetra tortor. Sed maximus ultrices pulvinar. In ex magna, molestie ac posuere id, aliquet quis enim. Donec a metus velit. Nulla lorem ipsum, molestie id augue ut, venenatis lobortis massa. Nam pulvinar scelerisque dignissim. Donec eu nunc quis purus fringilla cursus. Vestibulum ante ipsum primis in faucibus orci luctus et ultrices posuere cubilia Curae; Aliquam in interdum orci. Nam vitae augue nec metus congue placerat ut egestas est. Donec rhoncus mattis condimentum.</p>
      <p>Cras et leo vel mi aliquam dictum. Mauris ut cursus tellus, at dapibus sapien. Duis posuere augue nec ex congue semper. Donec a dolor fringilla, vulputate odio sit amet, pellentesque diam. Duis ultrices erat ligula, id aliquet magna facilisis dignissim. Ut molestie tristique eros eget ultrices. Nunc porta neque vitae odio elementum scelerisque. Suspendisse dapibus nisl sed augue tempor, sed dignissim dolor sagittis. Donec sed felis sollicitudin, consectetur metus id, egestas odio. In gravida purus non auctor congue. Donec augue mi, congue a euismod non, rhoncus non nibh. Fusce mauris neque, ultricies vitae ipsum nec, pharetra rhoncus mi. Maecenas ante nulla, egestas nec feugiat congue, fringilla eu dui.</p>
      <p>Nullam id euismod tellus. Fusce ultricies justo odio, in suscipit quam laoreet in. Quisque blandit orci eget nisi vulputate volutpat. Duis eget turpis facilisis, volutpat lectus sed, iaculis mi. Praesent tempor risus eget sodales tincidunt. Donec vitae nunc mauris. Pellentesque dignissim odio in nulla malesuada finibus. Integer porttitor odio ipsum, ac cursus quam facilisis eget. Suspendisse gravida felis quis metus pretium, non aliquet tellus consequat. Pellentesque ornare sapien sit amet arcu ultrices, sit amet tempor libero lacinia. Curabitur at ipsum quam. Aliquam eget velit vitae orci laoreet efficitur eget vel diam. Maecenas malesuada nibh metus. Vestibulum maximus urna et leo laoreet pellentesque.</p>
    </section>
  </main>

  <footer class="site-footer">© 2016 Brightmoor Labs. Al Right Reserved.</footer>
</body>
</html>
```